Lorna Vee Tresses Fancy Business Card’s

I want my business cards to be elite, original and very classy. I want the business cards to match the colors of my logo and to match the design posted. I would love the design of the picture I posted

I want the card all white .
The dripping on the top of the card I want it to match the pink color in my logo that’s also posted .
I need my logo on the business card !
I need my Instagram- @lorna.vee.tresses__
And my phone number - 555 207 9362

Target Market(s)

My target market is young woman age 23 to older woman to the age of 65
I want both older and younger women to love my design . I don’t want any cheap looking business cards

Industry/Entity Type

Hair And Beauty

Contact Information for Business Card

Add my logo
Add my Instagram- @lorna.vee.tresses__
My number - 555 207 9362
My website- www.lornaveetresses-example.com

Font styles to use
Serif
Script

Colors
ffffff
e667a6
e34298

Requirements
Must have
• The business cards must have my logo, my number , my website, and my Instagram!
Nice to have
• Nice to have glitter words that match my logo
• The business cards must look classy and mature
• I want them to be very unique!!
Should not have
• Should not have any colors that doesn’t match my logo ! This is very important! Please

```html
<!DOCTYPE html>
<html lang="en">
<head>
<meta charset="utf-8">
<title>Lorna Vee Tresses – Business Card</title>
<link rel="stylesheet" href="https://fonts.googleapis.com/css2?family=Open+Sans:wght@400&family=Playfair+Display:wght@600&display=swap">
<style>
  :root {
    --backdrop: #d9d8d5;
    --card: #ffffff;
    --pink: #e34298;
    --pink-soft: #e667a6;
    --ink: #555555;
    --shadow: rgba(0, 0, 0, 0.18);
  }
  * { box-sizing: border-box; margin: 0; padding: 0; }
  html, body {
    width: 1200px;
    height: 801px;
    overflow: hidden;
    background: var(--backdrop);
  }
  .canvas {
    position: relative;
    width: 1200px;
    height: 801px;
  }
  .card {
    position: absolute;
    top: 245px;
    width: 525px;
    height: 300px;
    background: var(--card);
    box-shadow: 0 10px 28px var(--shadow);
    overflow: hidden;
  }
  .card--contact { left: 50px; }
  .card--brand { left: 625px; }

  .brand-name {
    display: flex;
    align-items: center;
    gap: 10px;
    font-family: "Playfair Display", serif;
    font-weight: 600;
    color: var(--pink);
    white-space: nowrap;
    line-height: 1;
  }
  .brand-name__dot {
    width: 9px;
    height: 9px;
    border-radius: 50%;
    background: var(--pink);
    flex: none;
  }

  .card--contact .brand-name {
    position: absolute;
    left: 30px;
    top: 140px;
    font-size: 20px;
  }
  .divider {
    position: absolute;
    left: 252px;
    top: 95px;
    width: 1.5px;
    height: 110px;
    background: var(--pink);
  }
  .contact-list {
    position: absolute;
    left: 268px;
    top: 108px;
    list-style: none;
    font-family: "Open Sans", sans-serif;
    font-size: 12px;
    color: var(--ink);
    line-height: 28px;
  }
  .contact-list li {
    display: flex;
    align-items: center;
    gap: 7px;
    white-space: nowrap;
  }
  .contact-list svg { width: 11px; height: 11px; flex: none; }

  .card--brand .brand-name {
    position: absolute;
    left: 0;
    right: 0;
    top: 130px;
    justify-content: center;
    font-size: 36px;
  }
</style>
</head>
<body>
<main class="canvas">
  <section class="card card--contact" aria-label="Business card, contact side">
    <div class="brand-name"><span class="brand-name__dot"></span>Lorna Vee Tresses</div>
    <div class="divider"></div>
    <ul class="contact-list">
      <li>
        <svg viewBox="0 0 12 12" aria-hidden="true"><path d="M2.5 1 L4.5 1 L5.2 3.6 L4 4.6 Q5 7 7.4 8 L8.4 6.8 L11 7.5 L11 9.5 Q10.5 11 9 11 Q1 10 1 3 Q1 1.5 2.5 1 Z" fill="var(--pink)"/></svg>
        555 207 9362
      </li>
      <li>
        <svg viewBox="0 0 12 12" aria-hidden="true"><circle cx="6" cy="6" r="5" fill="none" stroke="var(--pink)" stroke-width="1.6"/></svg>
        @lorna.vee.tresses__
      </li>
      <li>
        <svg viewBox="0 0 12 12" aria-hidden="true"><circle cx="6" cy="6" r="5" fill="none" stroke="var(--pink)" stroke-width="1.3"/><ellipse cx="6" cy="6" rx="2.2" ry="5" fill="none" stroke="var(--pink)" stroke-width="1"/><line x1="1" y1="6" x2="11" y2="6" stroke="var(--pink)" stroke-width="1"/></svg>
        www.lornaveetresses-example.com
      </li>
    </ul>
  </section>

  <section class="card card--brand" aria-label="Business card, brand side">
    <div class="brand-name"><span class="brand-name__dot"></span>Lorna Vee Tresses</div>
  </section>
</main>
</body>
</html>
```